Tidewell Marketing company is looking for a web page design

Your projects should contain:

1. Header: Logo provided by us.
2. Top nav bar: offer, about us, experience, contact.
3. “Choose language” button.
4. Main section: panoramic picture (static, professional, modern).
5. Below section: 3 blocks (image+title+description), which represent our 3 main activities (titles):
• Market Research,
• Marketing Plans,
• Marketing Project.
6. ‘Contact us’ form – Message (text: “Write your message and give us details about your company and activities”), Email, SEND).
7. Page footer: (4 section: Contact, Social Media, Blog, Partners).
Updates

Hello!

I uploaded new file 'general_look', which is our idea how the page should generally look like.

BUT! it doesn't mean that your projects should look exactly like this project e.g.:
* titles Market Research, Marketing Plans, Marketing Project can be above these: Image 1,2,3.
* everything doesn't have to be in square and rectangle shape. You can try to manipulate with blocks and can add elipse elemnts or something similar.

We will appreciate your innovative ideas. Just wanted to give you general plan of the site and ilustrate all elements that we require.

Best Regards,
Benedek

IMPORTENT

Please remember that the main picture should be panoramic. Please do not close it in frame.

Target Market(s)

Small and middle sized companies, which would like to export their goods and services abroad and are interested in raising funds from Northgate Trade Council to expand their activities. These are rather industrial companies with low level of innovativeness. Our mission is to build image of the client’s company and increase awareness of their products to improve their competitiveness and innovativeness.

Industry/Entity Type

It Company

Requirements
Must have
• 1. Create designs of main page and subpage.
2. Subpage: Logo, Header, language button, place for article, navigation menu on the right side - below it “contact us” button , footer on the bottom. (In this section we are looking mainly for the design of the header and navigation menu).
3. The whole design should be a series of horizontal blocks.
4. Your projects should be associated with features such as: Reliability, Security, Professionalism, Openness, Uniqueness.
5. The design should be simple, fresh, readable, easy to use and should create a feeling of high quality services.
6. Possibility to change the panoramic picture (separate layer in a graphic file).
7. All pictures and blocks should be static, no movements.
8. Style of the page should be compliant with the logo design, font: Swiss.
9. Designs that we like: http://www.fernvale-studio.pl/, http://www.plumquarry.com/.
Should not have
• There shouldn’t be any distractions and not matching parts (whole design should be compact and easy to interpret and remember).

```html
<!DOCTYPE html>
<html lang="en">
<head>
<meta charset="utf-8">
<title>Tidewell Marketing</title>
<link rel="stylesheet" href="https://fonts.googleapis.com/css2?family=Arimo:ital,wght@0,400;0,700;1,400&display=swap">
<style>
  :root {
    --blue: #0d5189;
    --blue-dark: #083a66;
    --blue-light: #1e6aa8;
    --grey-btn-top: #d2d2d2;
    --grey-btn-bottom: #a9a9a9;
    --grey-text: #7a7a7a;
    --footer-bg: #ececec;
    --white: #ffffff;
    --ink: #1b3f66;
  }
  * { box-sizing: border-box; margin: 0; padding: 0; }
  html, body { width: 766px; height: 1200px; overflow: hidden; background: var(--white); }
  body { font-family: "Arimo", Arial, sans-serif; position: relative; }

  .brand { position: absolute; left: 25px; top: 22px; }
  .brand-name { font-size: 25px; font-weight: 700; color: var(--ink); line-height: 1; }

  .lang-btn {
    position: absolute; left: 582px; top: 20px; width: 164px; height: 32px;
    background: linear-gradient(var(--grey-btn-top), var(--grey-btn-bottom));
    color: var(--white); font-size: 13px; font-weight: 700;
    display: flex; align-items: center; justify-content: center; letter-spacing: 0.3px;
  }

  .main-nav { position: absolute; left: 332px; top: 79px; width: 414px; height: 36px; display: flex; gap: 4px; }
  .main-nav a {
    flex: auto; background: linear-gradient(var(--blue-light), var(--blue-dark));
    color: var(--white); text-decoration: none; font-size: 13px; font-weight: 700;
    display: flex; align-items: center; justify-content: center;
  }
  .main-nav a:first-child { border-radius: 8px 0 0 8px; }
  .main-nav a:last-child { border-radius: 0 8px 8px 0; }

  .hero {
    position: absolute; left: 25px; top: 148px; width: 721px; height: 304px;
    background: linear-gradient(180deg, #3f7fc4 0%, #7fb2e2 45%, #d9e8f5 75%, #f3f7fb 100%);
  }

  .activities { position: absolute; left: 25px; top: 498px; width: 721px; display: flex; gap: 25px; }
  .activity { width: 224px; height: 345px; background: linear-gradient(var(--blue), var(--blue-dark)); color: var(--white); }
  .activity-image { height: 162px; }
  .activity-image.research { background: linear-gradient(160deg, #8fc0e6, #6f9a3e 80%); }
  .activity-image.plans { background: linear-gradient(160deg, #fafafa, #d8d8d8); }
  .activity-image.project { background: radial-gradient(circle at 50% 50%, #6a5a3a 0%, #2c3c5a 45%, #e9e9e9 60%); }
  .activity-title {
    height: 68px; display: flex; align-items: center; justify-content: center; text-align: center;
    font-size: 18px; font-weight: 700; line-height: 1.15; border-bottom: 1px solid rgba(255,255,255,0.25);
  }
  .activity-text { padding: 10px 16px; font-size: 10.5px; line-height: 1.35; }

  .message {
    position: absolute; left: 25px; top: 862px; width: 358px; height: 133px;
    background: linear-gradient(var(--blue-light), var(--blue-dark)); color: var(--white);
    border-radius: 6px;
  }
  .message-title { height: 44px; display: flex; align-items: center; justify-content: center; font-size: 21px; font-weight: 700; border-bottom: 1px solid rgba(255,255,255,0.3); }
  .message-text { padding: 12px 30px; font-size: 15px; font-style: italic; line-height: 1.3; }

  .form-field {
    position: absolute; left: 429px; width: 317px; height: 53px; border-radius: 4px;
    background: linear-gradient(var(--grey-btn-top), var(--grey-btn-bottom));
    color: var(--grey-text); font-size: 21px; font-weight: 700;
    display: flex; align-items: center; justify-content: center; letter-spacing: 0.5px;
  }
  .form-field.email { top: 862px; }
  .form-field.send { top: 937px; }

  .site-footer { position: absolute; left: 25px; top: 1025px; width: 721px; height: 175px; background: var(--footer-bg); }
  .footer-heads { display: flex; height: 35px; background: linear-gradient(var(--blue-light), var(--blue-dark)); }
  .footer-heads div { flex: 1; color: var(--white); font-size: 15px; display: flex; align-items: center; justify-content: center; border-right: 1px solid rgba(255,255,255,0.4); }
  .footer-heads div:last-child { border-right: 0; }
  .footer-cols { display: flex; }
  .footer-cols ul { flex: 1; list-style: none; padding: 14px 0 0 28px; border-right: 1px solid #d4d4d4; height: 140px; }
  .footer-cols ul:last-child { border-right: 0; }
  .footer-cols li { font-size: 11px; color: #9a9a9a; line-height: 22px; letter-spacing: 2px; }
  .footer-cols li::before { content: "\2022"; margin-right: 8px; color: #8a8a8a; }
</style>
</head>
<body>
  <header>
    <div class="brand">
      <div class="brand-name">Tidewell Marketing</div>
    </div>
    <div class="lang-btn">CHOOSE LANGUAGE</div>
    <nav class="main-nav">
      <a href="#">OFFER</a><a href="#">ABOUT US</a><a href="#">EXPERIENCE</a><a href="#">CONTACT</a>
    </nav>
  </header>

  <div class="hero" role="img" aria-label="Panoramic photo of green street signs reading Marketing Ave and Strategy St against a blue sky with clouds"></div>

  <section class="activities">
    <article class="activity">
      <div class="activity-image research" role="img" aria-label="Photo of a hand holding a smartphone over a green field"></div>
      <h2 class="activity-title">MARKET<br>RESEARCH</h2>
      <p class="activity-text">Lorem ipsum dolor sit amet, consectetur adipiscing elit, sed do eiusmod tempor incididunt ut labore et dolore magna aliqua. Ut enim ad minim veniam, quis nostrud exercitation ullamco laboris nisi ut aliquip ex ea commodo consequat.</p>
    </article>
    <article class="activity">
      <div class="activity-image plans" role="img" aria-label="Photo of a hand drawing a strategy diagram with words like excellence, finance and innovation"></div>
      <h2 class="activity-title">MARKETING<br>PLANS</h2>
      <p class="activity-text">Lorem ipsum dolor sit amet, consectetur adipiscing elit, sed do eiusmod tempor incididunt ut labore et dolore magna aliqua. Ut enim ad minim veniam, quis nostrud exercitation ullamco laboris nisi ut aliquip ex ea commodo consequat.</p>
    </article>
    <article class="activity">
      <div class="activity-image project" role="img" aria-label="Photo of a globe made of many small photographs"></div>
      <h2 class="activity-title">MARKETING<br>PROJECT</h2>
      <p class="activity-text">Lorem ipsum dolor sit amet, consectetur adipiscing elit, sed do eiusmod tempor incididunt ut labore et dolore magna aliqua. Ut enim ad minim veniam, quis nostrud exercitation ullamco laboris nisi ut aliquip ex ea commodo consequat.</p>
    </article>
  </section>

  <section class="message">
    <h2 class="message-title">MESSAGE</h2>
    <p class="message-text">Write your message and give details about your company and activities.</p>
  </section>
  <div class="form-field email">EMAIL</div>
  <div class="form-field send">SEND</div>

  <footer class="site-footer">
    <div class="footer-heads">
      <div>CONTACT</div><div>SOCIAL MEDIA</div><div>BLOG</div><div>PARTNERS</div>
    </div>
    <div class="footer-cols">
      <ul><li>.......</li><li>.......</li><li>.......</li><li>.......</li><li>.......</li></ul>
      <ul><li>.......</li><li>.......</li><li>.......</li><li>.......</li><li>.......</li></ul>
      <ul><li>.......</li><li>.......</li><li>.......</li><li>.......</li><li>.......</li></ul>
      <ul><li>.......</li><li>.......</li><li>.......</li><li>.......</li><li>.......</li></ul>
    </div>
  </footer>
</body>
</html>
```